independent cleaner, reliable, custom, thorough, trustworthy

Not sure yet if I want single-sided or double sided, so I'm selecting double-sided just in case, but single-sided designs are okay.

Really looking to find the happy medium between personal and professional in a business card design. I end up building comfortable relationships with the people I work for.

Most of my business is through referrals, but I want some business cards to hand out to people who ask for one (and maybe put them on community bulletin boards).

My target market is homeowners and business owners who are looking for a reliable cleaner and are willing to pay a bit more to have excellent quality and someone they trust.

Theme: I have a personal-professional feel since I'm solo, so the theme should reflect that. Trustworthy, personal, simple. I clean up messes.

Hopefully this is enough info, let me know if you have any questions though of course!

Target Market(s)

Homeowners businessowners who are looking for a reliable cleaner, excellent quality trustworthy.

Industry/Entity Type

Cleaning Service

Contact Information for Business Card

Please include this text:
• Delphine Warrow
• independent cleaner
• reliable, custom, thorough
• 604-317-2269
• mtb.warrow@postmail.example

Font styles to use
Serif
Sans Serif

Colors
ffffff
00a990
0492cd
33a6d7
0355a3
3276b5
919191

Requirements
Must have
• Really looking to find the happy medium between personal and professional in a business card design.
• Background: at least 50% white on the side with the most text (coloured accents or shapes are okay)
• I lean more towards simple and clean, solid colours, maybe a gentle gradient
Nice to have
• Not sure yet if I want single-sided or double sided, so I'm selecting double-sided just in case, but single-sided designs are okay.
• Colours: preferably blues and teals for the font and other objects (if any). Open to designer's choice though. I've toyed around with orangey-yellow, but it doesn't feel right and I keep going back to blues/teals
• Also I uploaded a sketch of my signature and initials so you can get a feel for my personality. I'm not expecting this to be included in the design, it's just there.
Should not have
• I don't like a lot of busy-ness or textures
• Also I don't have a logo (not sure where else to specify this)

```html
<!DOCTYPE html>
<html lang="en">
<head>
<meta charset="utf-8">
<title>Delphine Warrow – Business Card</title>
<link href="https://fonts.googleapis.com/css2?family=Noto+Serif:wght@400;700&display=swap" rel="stylesheet">
<style>
  :root {
    --stage: #26292d;
    --paper: #ffffff;
    --ink: #1a1a1a;
    --blue: #1690cf;
    --blue-light: #33a6d7;
    --blue-deep: #0f86c6;
  }
  * { box-sizing: border-box; margin: 0; padding: 0; }
  html, body {
    width: 1200px; height: 900px; overflow: hidden;
    background: var(--stage);
    font-family: "Noto Serif", Georgia, serif;
  }
  .stage {
    width: 1200px; height: 900px;
    display: flex; flex-direction: column;
    align-items: center; justify-content: center;
    gap: 48px;
  }
  .card {
    position: relative;
    width: 602px; height: 344px;
    background: var(--paper);
    overflow: hidden;
    box-shadow: 0 10px 28px rgba(0,0,0,.45);
  }

  /* Front: contact side */
  .card-front .details {
    position: absolute;
    left: 150px; top: 70px;
    color: var(--ink);
  }
  .name {
    font-size: 30px; font-weight: 700; letter-spacing: .2px;
    line-height: 1.1;
    margin-left: 115px;
  }
  .role {
    font-size: 17px; font-weight: 400;
    margin-left: 115px; margin-top: 2px;
  }
  .tagline-row {
    display: flex; align-items: center; gap: 12px;
    margin-top: 18px; margin-left: -62px;
  }
  .dots { display: flex; align-items: center; gap: 6px; }
  .dots span { display: block; border-radius: 50%; background: var(--blue); }
  .dots .d1 { width: 11px; height: 11px; }
  .dots .d2 { width: 14px; height: 14px; }
  .dots .d3 { width: 17px; height: 17px; }
  .tagline {
    background: var(--blue);
    color: var(--paper);
    font-size: 18px;
    padding: 8px 26px;
    border-radius: 22px;
    white-space: nowrap;
  }
  .contact { margin-top: 20px; font-size: 18px; line-height: 1.5; }

  /* Back: brand side */
  .card-back .band {
    position: absolute;
    left: 0; right: 0; top: 176px; bottom: 0;
    background: linear-gradient(115deg, var(--blue-deep) 0%, var(--blue-light) 100%);
  }
  .card-back .seal {
    position: absolute;
    left: 155px; top: 66px;
    width: 220px; height: 220px;
    border-radius: 50%;
    background: var(--paper);
    display: flex; align-items: center; justify-content: center;
    text-align: center;
  }
  .seal-name {
    font-size: 26px; font-weight: 700; color: var(--blue);
    line-height: 1.2;
  }
</style>
</head>
<body>
<main class="stage">
  <section class="card card-front" aria-label="Business card front">
    <div class="details">
      <p class="name">Delphine Warrow</p>
      <p class="role">Independent Cleaner</p>
      <div class="tagline-row">
        <div class="dots"><span class="d1"></span><span class="d2"></span><span class="d3"></span></div>
        <p class="tagline">Reliable, Custom, Thorough</p>
        <div class="dots"><span class="d3"></span><span class="d2"></span><span class="d1"></span></div>
      </div>
      <div class="contact">
        <p class="phone">604-317-2269</p>
        <p class="email">mtb.warrow@postmail.example</p>
      </div>
    </div>
  </section>

  <section class="card card-back" aria-label="Business card back">
    <div class="band"></div>
    <div class="seal">
      <p class="seal-name">Delphine<br>Warrow</p>
    </div>
  </section>
</main>
</body>
</html>
```